Marwick Ostrand Law website for a law firm

modern clean website for a small boutique law firm. Based in Sacramento, CA and the Bay Area. Practice areas of Family Law, Civil litigation, and Criminal Defense. We already have a logo design as well as attorney pictures to include on page.
Would like images of California included on site.
Would like site to go with Logo that is already designed...blue/grey/white colors.

Industry/Entity Type

Law Firm

Number of Pages Required

5+ page

Requirements
Must have
• I already have several pages of content drafted. Just need the pages with images to input content. Must be clean and modern feel. Want it to reflect California and small boutique feel that is provided personalized legal attention.
• Must have a page where I can blog or post articles on.

```html
<!DOCTYPE html>
<html lang="en">
<head>
<meta charset="utf-8">
<title>Marwick Ostrand Law Firm</title>
<link href="https://fonts.googleapis.com/css2?family=Lora:wght@400;700&family=Open+Sans:wght@400;600;700&display=swap" rel="stylesheet">
<style>
:root{
  --blue:#4a86c9;
  --blue-deep:#3c70b2;
  --ink:#2c2c2c;
  --muted:#777;
  --line:#e2e2e2;
  --light:#eef0f3;
  --white:#fff;
  --red:#c0392b;
  --dark:#3b3b3d;
  --night:#1c2231;
}
*{box-sizing:border-box;margin:0;padding:0}
html,body{width:1200px;height:3814px;overflow:hidden}
body{position:relative;background:var(--white);font-family:"Open Sans",sans-serif;color:var(--ink)}
.abs{position:absolute}

/* header / hero */
.hero{left:0;top:0;width:1200px;height:560px;background:linear-gradient(100deg,#3a2a22 0%,#5b4232 35%,#6b4b36 60%,#4a372c 100%)}
.logo{left:97px;top:30px;font-family:"Lora",serif;font-size:58px;font-weight:400;color:var(--white);letter-spacing:1px}
.consult-btn{left:735px;top:24px;width:190px;height:42px;border:2px solid var(--white);border-radius:21px;background:#1b1b1b;color:var(--white);font-family:"Lora",serif;font-weight:700;font-size:14px;display:flex;align-items:center;justify-content:center}
.phone{left:950px;top:32px;color:var(--white);font-size:17px;display:flex;align-items:center;gap:12px}
.nav{left:672px;top:88px;display:flex;gap:40px;font-family:"Lora",serif;font-weight:700;font-size:13px;color:var(--white)}
.nav .active{color:#8fb6e6}
.hero-title{left:466px;top:330px;font-family:"Lora",serif;font-weight:700;font-size:49px;color:var(--white)}
.hero-sub{left:466px;top:425px;font-family:"Lora",serif;font-size:24px;letter-spacing:1.5px;color:#eee}

/* about band */
.about-band{left:0;top:515px;width:1200px;height:545px;background:linear-gradient(180deg,#5c93d2 0%,#4a86c9 55%,#3f77ba 100%);clip-path:polygon(0 12%,22% 5%,44% 8%,63% 0,82% 6%,100% 2%,100% 94%,80% 97%,58% 91%,36% 100%,16% 94%,0 98%)}
.about-photo{left:97px;top:590px;width:305px;height:305px;border-radius:50%;border:4px solid var(--white);background:linear-gradient(180deg,#a8c8e6 0%,#c9a46e 48%,#3f6f8f 60%,#5c4f45 100%)}
.about-title{left:427px;top:650px;font-family:"Lora",serif;font-weight:700;font-size:30px;color:var(--white)}
.about-text{left:427px;top:715px;width:330px;font-size:11.5px;line-height:20px;color:#eaf1fa}
.about-text p+p{margin-top:14px}
.btn-ghost{left:427px;top:928px;width:133px;height:38px;border:1.5px solid var(--white);border-radius:19px;color:var(--white);font-family:"Lora",serif;font-weight:700;font-size:12px;display:flex;align-items:center;justify-content:center}
.form-box{left:788px;top:661px;width:312px;height:300px;background:#f2f5f9;padding:24px 22px}
.form-box h3{font-family:"Lora",serif;font-weight:700;font-size:13px;margin-bottom:14px}
.field{height:40px;border-bottom:1px solid #d5dbe3;display:flex;justify-content:space-between;align-items:center;font-size:11px;color:#888}
.field svg{width:14px;height:14px;fill:var(--blue)}
.submit{margin-top:18px;width:100px;height:32px;border-radius:16px;background:var(--blue);color:var(--white);font-family:"Lora",serif;font-weight:700;font-size:12px;display:flex;align-items:center;justify-content:center}

/* meet section */
.meet-band{left:0;top:1040px;width:1200px;height:520px;background:linear-gradient(135deg,#f4f5f7 0%,#e4e7eb 40%,#f2f3f5 70%,#e1e4e8 100%)}
.meet-title{left:97px;top:1150px;font-family:"Lora",serif;font-weight:700;font-size:28px}
.meet-text{left:97px;top:1215px;width:430px;font-size:11.5px;line-height:20px;color:var(--muted)}
.meet-text p+p{margin-top:20px}
.btn-blue{left:97px;top:1432px;width:133px;height:40px;border-radius:20px;background:var(--blue);color:var(--white);font-family:"Lora",serif;font-weight:700;font-size:12px;display:flex;align-items:center;justify-content:center}
.meet-image{left:491px;top:1151px;width:617px;height:342px;background:linear-gradient(180deg,#5a5e66 0%,#c9ccd1 55%,#9a9ea4 100%)}

/* practice */
.section-title{width:1200px;left:0;text-align:center;font-family:"Lora",serif;font-weight:700;font-size:28px}
.card{width:322px;height:282px;border:1px solid var(--line);background:var(--white)}
.card-img{width:100%;height:202px;background:linear-gradient(135deg,#8a6d58,#c2a184 50%,#5e6c7c)}
.card-label{height:80px;display:flex;align-items:center;justify-content:center;font-family:"Lora",serif;font-weight:700;font-size:17px}

/* testimonial */
.testi-band{left:0;top:2030px;width:1200px;height:515px;background:linear-gradient(90deg,#3d3d40,#58585c 30%,#4a4a4e 60%,#3a3a3d);clip-path:polygon(0 3%,20% 0,40% 4%,62% 0,82% 4%,100% 1%,100% 96%,78% 100%,56% 95%,36% 99%,16% 95%,0 99%)}
.quote{left:0;width:1200px;top:2120px;display:flex;justify-content:center}
.testi-text{left:280px;top:2195px;width:640px;text-align:center;font-size:11.5px;line-height:22px;color:#eee}
.avatar{left:555px;top:2300px;width:90px;height:90px;border-radius:50%;border:4px solid var(--white);background:linear-gradient(#c9a48a,#6b4d3d)}
.person{left:0;width:1200px;top:2402px;text-align:center;color:#ddd;font-size:13px;line-height:20px}
.dots{left:0;width:1200px;top:2482px;display:flex;justify-content:center;gap:8px}
.dots span{width:10px;height:10px;border-radius:50%;border:1.5px solid var(--white)}
.dots span.on{background:var(--white)}

/* blog */
.post{width:322px;height:268px;border:1px solid var(--line);background:var(--white)}
.post-img{position:relative;height:190px;background:linear-gradient(135deg,#6b5646,#b89a7e 55%,#3f4f60)}
.date{position:absolute;right:0;top:0;display:flex}
.date .m{width:50px;height:36px;background:rgba(255,255,255,.9);font-family:"Lora",serif;font-size:14px;display:flex;align-items:center;justify-content:center}
.date .d{width:40px;height:36px;background:var(--blue);color:var(--white);font-family:"Lora",serif;font-weight:700;font-size:14px;display:flex;align-items:center;justify-content:center}
.post-body{padding:12px 20px;font-size:11px;line-height:18px;color:var(--muted)}
.post-body a{display:inline-block;margin-top:6px;color:var(--red);font-size:11px;text-decoration:underline}

/* firms */
.firms-rule{left:0;top:3080px;width:1200px;height:1px;background:var(--line)}
.firm{width:158px;height:102px;border:1px solid var(--line);display:flex;align-items:center;justify-content:center}
.firm span{width:120px;height:70px;background:#e4e6e9}

/* footer */
.footer{left:0;top:3406px;width:1200px;height:408px;background:linear-gradient(180deg,#2a3346 0%,#1c2231 60%,#151a26 100%)}
.f-logo{left:97px;top:3470px;font-family:"Lora",serif;font-size:54px;color:var(--white)}
.f-head{font-family:"Lora",serif;font-weight:700;font-size:16px;color:var(--white);letter-spacing:.5px}
.f-about{left:97px;width:260px;font-size:11px;line-height:18px;color:#cfd4dc}
.f-links{list-style:none;color:#cfd4dc;font-size:11px}
.f-links li{height:37px;display:flex;align-items:center;gap:14px}
.f-links li::before{content:"";width:9px;height:9px;border-radius:50%;background:#cfd4dc}
.email{left:844px;top:3517px;width:256px;height:36px;display:flex}
.email .in{flex:1;background:var(--white);font-size:11px;color:#777;display:flex;align-items:center;padding-left:12px}
.email .go{width:80px;background:var(--blue);color:var(--white);font-weight:700;font-size:13px;display:flex;align-items:center;justify-content:center}
.social{left:844px;top:3646px;display:flex;gap:10px}
.social span{width:30px;height:30px;border-radius:50%}
.copy-rule{left:0;top:3745px;width:1200px;height:1px;background:rgba(255,255,255,.15)}
.copy{left:0;top:3766px;width:1200px;text-align:center;font-size:12px;color:#cfd4dc}
</style>
</head>
<body>

<!-- header / hero -->
<div class="abs hero" role="img" aria-label="Smiling attorney in a suit in front of a law library bookshelf"></div>
<div class="abs logo">MOLAW</div>
<div class="abs consult-btn">Call For Free Consultation</div>
<div class="abs phone">
  <svg width="16" height="16" viewBox="0 0 24 24" fill="#fff"><path d="M6.6 10.8a15.1 15.1 0 0 0 6.6 6.6l2.2-2.2c.3-.3.7-.4 1-.2 1.1.4 2.3.6 3.6.6.6 0 1 .4 1 1V20c0 .6-.4 1-1 1A17 17 0 0 1 3 4c0-.6.4-1 1-1h3.5c.6 0 1 .4 1 1 0 1.3.2 2.5.6 3.6.1.3 0 .7-.2 1z"/></svg>
  <span>555-0142-7731</span>
</div>
<nav class="abs nav"><span class="active">HOME</span><span>ABOUT</span><span>PRACTICE AREAS</span><span>BLOG</span><span>CONTACT</span></nav>
<h1 class="abs hero-title">Marwick Ostrand Law Firm</h1>
<div class="abs hero-sub">Excepteur sint occaecat cupidatat non proident</div>

<!-- about -->
<div class="abs about-band" role="img" aria-label="Blue tinted shelf of law books"></div>
<div class="abs about-photo" role="img" aria-label="Golden Gate Bridge above a rocky California shoreline"></div>
<h2 class="abs about-title">About US</h2>
<div class="abs about-text">
  <p>Sed ut perspiciatis unde omnis iste natus error sit voluptatem accusantium doloremque laudantium, totam rem aperiam eaque ipsa quae ab illo inventore veritatis et quasi architecto beatae vitae dicta.</p>
  <p>Sunt explicabo. Nemo enim ipsam voluptatem quia voluptas sit aspernatur aut odit aut fugit, sed quia consequuntur.</p>
</div>
<div class="abs btn-ghost">READ MORE</div>
<form class="abs form-box">
  <h3>MAKE A FREE CONSULTATION</h3>
  <div class="field"><span>Name</span><svg viewBox="0 0 24 24"><circle cx="12" cy="7" r="5"/><path d="M2 22c0-6 4-9 10-9s10 3 10 9z"/></svg></div>
  <div class="field"><span>Phone</span><svg viewBox="0 0 24 24"><path d="M6.6 10.8a15.1 15.1 0 0 0 6.6 6.6l2.2-2.2c.3-.3.7-.4 1-.2 1.1.4 2.3.6 3.6.6.6 0 1 .4 1 1V20c0 .6-.4 1-1 1A17 17 0 0 1 3 4c0-.6.4-1 1-1h3.5c.6 0 1 .4 1 1 0 1.3.2 2.5.6 3.6.1.3 0 .7-.2 1z"/></svg></div>
  <div class="field"><span>Email</span><svg viewBox="0 0 24 24"><path d="M2 5h20v14H2z"/></svg></div>
  <div class="field"><span>How Can We Help You ?</span><svg viewBox="0 0 24 24"><path d="M3 4h18v12H8l-5 4z"/></svg></div>
  <div class="submit">SUBMIT</div>
</form>

<!-- meet -->
<div class="abs meet-band"></div>
<h2 class="abs meet-title">Meet Your Lawyer Realtime</h2>
<div class="abs meet-text">
  <p>Sed ut perspiciatis unde omnis iste natus error sit voluptatem accusantium doloremque laudantium, totam rem aperiam, eaque ipsa quae inventore veritatis et quasi architecto beatae vitae dicta sunt explicabo. Nemo enim ipsam voluptatem.</p>
  <p>Magni dolores eos qui ratione voluptatem sequi nesciunt. Neque porro quisquam est, qui dolorem ipsum quia dolor sit amet, consectetur, adipisci velit, sed quia non numquam eius modi tempora.</p>
</div>
<div class="abs btn-blue">Read More</div>
<div class="abs meet-image" role="img" aria-label="Laptop showing a live video consultation with an attorney"></div>

<!-- practice areas -->
<h2 class="abs section-title" style="top:1608px">Practice Areas</h2>
<div class="abs card" style="left:97px;top:1693px"><div class="card-img" role="img" aria-label="Family reading together"></div><div class="card-label">Family Law</div></div>
<div class="abs card" style="left:439px;top:1693px"><div class="card-img" role="img" aria-label="Officers at a civil dispute"></div><div class="card-label">Civil litigation law</div></div>
<div class="abs card" style="left:779px;top:1693px"><div class="card-img" role="img" aria-label="Client meeting with defense counsel"></div><div class="card-label">Criminal Defense law</div></div>

<!-- testimonial -->
<div class="abs testi-band" role="img" aria-label="Grid of client portraits in grey tones"></div>
<div class="abs quote"><svg width="52" height="40" viewBox="0 0 52 40" fill="#fff"><path d="M0 40V22C0 9 7 2 20 0l2 5c-7 2-10 6-10 13h10v22zM30 40V22C30 9 37 2 50 0l2 5c-7 2-10 6-10 13h10v22z"/></svg></div>
<p class="abs testi-text">Lorem ipsum dolor sit amet, consectetur adipiscing elit, sed do eiusmod tempor incididunt ut labore et dolore magna aliqua. Ut enim ad minim veniam, quis nostrud exercitation ullamco laboris nisi ut aliquip ex ea commodo consequat. Duis aute irure dolor in reprehenderit in voluptate velit esse cillum.</p>
<div class="abs avatar" role="img" aria-label="Client portrait"></div>
<div class="abs person">- Person Name<br>- City Location</div>
<div class="abs dots"><span class="on"></span><span></span><span class="on"></span></div>

<!-- blog -->
<h2 class="abs section-title" style="top:2594px">Blog Post</h2>
<article class="abs post" style="left:97px;top:2682px">
  <div class="post-img" role="img" aria-label="Business meeting at a table"><div class="date"><span class="m">Sep</span><span class="d">03</span></div></div>
  <div class="post-body">Sed ut perspiciatis unde omnis iste natus error sit voluptatem accusantium doloremque laudantium, totam rem aperiam, eaque<br><a>Read More...</a></div>
</article>
<article class="abs post" style="left:439px;top:2682px">
  <div class="post-img" role="img" aria-label="Courtroom hearing"><div class="date"><span class="m">Sep</span><span class="d">03</span></div></div>
  <div class="post-body">Sed ut perspiciatis unde omnis iste natus error sit voluptatem accusantium doloremque laudantium, totam rem aperiam, eaque<br><a>Read More...</a></div>
</article>
<article class="abs post" style="left:779px;top:2682px">
  <div class="post-img" role="img" aria-label="Family consulting an attorney"><div class="date"><span class="m">Sep</span><span class="d">03</span></div></div>
  <div class="post-body">Sed ut perspiciatis unde omnis iste natus error sit voluptatem accusantium doloremque laudantium, totam rem aperiam, eaque<br><a>Read More...</a></div>
</article>

<!-- featured firms -->
<div class="abs firms-rule"></div>
<h2 class="abs section-title" style="top:3115px">Featured Firms</h2>
<div class="abs firm" style="left:97px;top:3198px"><span></span></div>
<div class="abs firm" style="left:301px;top:3198px"><span></span></div>
<div class="abs firm" style="left:503px;top:3198px"><span></span></div>
<div class="abs firm" style="left:705px;top:3198px"><span></span></div>
<div class="abs firm" style="left:907px;top:3198px"><span></span></div>

<!-- footer -->
<footer class="abs footer" role="img" aria-label="San Francisco skyline and bridge at night"></footer>
<div class="abs f-logo">MOLAW</div>
<div class="abs f-head" style="left:97px;top:3556px">ABOUT US</div>
<p class="abs f-about" style="top:3590px">Nam eu nisi non quam ultrices lacinia. Nam convallis, ex at consectetur tempor. Nullam fringilla mattis vestibulum auctor lacus ac consectetur suspendisse vel interdum neque.</p>
<div class="abs f-head" style="left:437px;top:3478px">HELP LINKS</div>
<ul class="abs f-links" style="left:437px;top:3512px"><li>Home</li><li>About Us</li><li>Blog</li><li>Testimonials</li></ul>
<div class="abs f-head" style="left:620px;top:3478px">OTHER LINKS</div>
<ul class="abs f-links" style="left:620px;top:3512px"><li>Terms &amp; Conditions</li><li>Privacy Policy</li><li>Contact Us</li><li>Legal Activism</li></ul>
<div class="abs f-head" style="left:844px;top:3478px">JOIN US</div>
<div class="abs email"><span class="in">Email ID...</span><span class="go">SEND</span></div>
<div class="abs f-head" style="left:844px;top:3603px">FOLLOW US</div>
<div class="abs social"><span style="background:#3b5b9a"></span><span style="background:#2aa3e0"></span><span style="background:#d6443a"></span></div>
<div class="abs copy-rule"></div>
<div class="abs copy">Copyright © Marwick Ostrand Law Firm, 2017.All rights reserved.</div>

</body>
</html>
```